Firm of surveyors needs a professional yet friendly looking flyer

Our company offers help to landlords who have a phone mast on their property. We help them to negotiate the best rent and lease terms. There are so many landlords who don't seek professional advice because they don't know it's available. We want to send them a flyer which is informative, looks professional but also friendly so it prompts them to call us. I have attached the wording and some pictures but have more I can send but they were too large to attach.

Target Market(s)

Ranges from farmers to large corporations and land owners

Industry/Entity Type

Surveyor

Font styles to use
Sans Serif

Colors
acd136
9bcb3c
000000
ffffff
606060
848484

Requirements
Must have
• Must be clear, must give a professional look, must include pictures, must include our logo, must use our colour scheme (or variations of it). Ideally, I would like a try-fold design if possible.
Nice to have
• I would like there to be stand out lines to catch the readers eye (I have included some on the wording document). I would like a clean and modern design
Should not have
• Should not be too fussy

```html
<!DOCTYPE html>
<html lang="en">
<head>
<meta charset="utf-8">
<title>Tallpoint Mast Advisers – Tri-fold Flyer</title>
<link href="https://fonts.googleapis.com/css2?family=Nunito:wght@800;900&family=Raleway:wght@400;600;700&display=swap" rel="stylesheet">
<style>
  :root{
    --lime:#acd136;
    --green:#9bcb3c;
    --green-deep:#7fb02a;
    --black:#000000;
    --white:#ffffff;
    --grey:#606060;
    --grey-light:#848484;
    --paper:#f4f5f3;
    --board:#22381a;
    --board-label:#4d6d2c;
    --sky-top:#2d6fd0;
    --sky-low:#bcd9f2;
  }
  *{box-sizing:border-box;margin:0;padding:0}
  html,body{width:797px;height:1200px;overflow:hidden}
  body{background:var(--board);font-family:"Raleway",sans-serif;color:var(--grey);position:relative}
  .board-label{position:absolute;left:0;width:797px;text-align:center;font-family:"Nunito",sans-serif;font-weight:900;font-size:17px;color:var(--board-label);letter-spacing:.3px}
  .board-label.outer{top:52px}
  .board-label.inner{top:1130px}

  .spread{position:absolute;left:82px;width:633px;height:489px;display:flex;box-shadow:0 4px 14px rgba(0,0,0,.35)}
  .spread.outer{top:94px}
  .spread.inner{top:620px}
  .panel{position:relative;width:211px;height:489px;overflow:hidden}
  .panel.white{background:var(--white)}
  .panel.paper{background:var(--paper)}
  .panel.lime{background:var(--green)}

  .heading{font-family:"Nunito",sans-serif;font-weight:900;color:var(--green);line-height:1}
  .body-copy{font-size:6.6px;line-height:11.2px;text-align:justify;color:var(--grey)}
  .body-copy p+p{margin-top:13px}
  .body-copy strong{font-weight:700}
  .body-copy .accent{color:var(--green);font-weight:700}

  .abs{position:absolute}
  .fill-svg{position:absolute;left:0;top:0}

  /* outer panel 1 */
  .climate-title{left:21px;top:28px;font-size:14px}
  .climate-copy{left:21px;top:70px;width:169px}
  .callout{left:19px;top:500px;top:402px;width:185px;font-family:"Nunito",sans-serif;font-weight:900;font-size:13.4px;line-height:14px;color:var(--white)}

  /* outer panel 2 */
  .services-title{left:19px;top:30px;font-size:19px}
  .service-list{left:24px;top:66px;list-style:none;font-size:8.9px;line-height:14.4px;color:var(--grey)}
  .service-list li{position:relative;padding-left:13px}
  .service-list li::before{content:"";position:absolute;left:0;top:5px;width:4px;height:4px;border-radius:50%;background:var(--green)}
  .contact-title{left:19px;top:232px;font-size:19px}
  .contact-list{left:24px;top:268px;list-style:none;font-size:8.9px;line-height:14.4px;color:var(--grey)}
  .contact-list li{position:relative;padding-left:14px}
  .contact-list svg{position:absolute;left:0;top:3px}
  .brand-mark{display:flex;align-items:center;gap:5px;font-family:"Nunito",sans-serif;font-weight:900}
  .brand-mark .dot{width:9px;height:9px;border-radius:50%;background:var(--green);flex:none}
  .brand-back{left:46px;top:432px;font-size:13px;color:#3c3c3c;line-height:1.05}

  /* outer panel 3 */
  .brand-front{left:40px;top:30px;font-size:16px;color:var(--white);line-height:1.05}
  .brand-front .dot{background:var(--white)}
  .cover-headline{left:0;width:211px;top:336px;text-align:center;font-family:"Nunito",sans-serif;font-weight:900;color:var(--white);line-height:1}
  .cover-headline .big{display:block;font-size:35px;letter-spacing:.5px}
  .cover-headline .mid{display:block;font-size:15.5px;margin-top:2px}
  .cover-rule{left:21px;top:417px;width:169px;height:1px;background:rgba(255,255,255,.55)}
  .cover-promise{left:0;width:211px;top:425px;text-align:center;font-size:9.4px;line-height:12px;color:var(--white);font-weight:600}
  .web-pill{left:26px;top:470px;width:160px;height:19px;border-radius:9px 9px 0 0;background:var(--lime);display:flex;align-items:center;justify-content:center;gap:5px;font-size:7.6px;font-weight:700;color:var(--white)}

  /* inner panel 1 */
  .firm-title{left:20px;top:27px;width:180px;font-size:13.6px;line-height:14.4px}
  .firm-copy{left:20px;top:127px;width:169px}

  /* inner panel 2 */
  .lease-copy{left:20px;top:26px;width:170px;color:var(--white)}
  .lease-copy.second{top:261px}
  .sell-title{left:20px;top:386px;font-size:13.6px;color:var(--white)}
  .sell-copy{left:20px;top:408px;width:170px;color:var(--white)}

  /* inner panel 3 */
  .cash-copy{left:23px;top:258px;width:169px}
  .getting-title{left:23px;top:346px;font-size:13.6px}
  .getting-copy{left:23px;top:368px;width:169px}
</style>
</head>
<body>

<div class="board-label outer">OUTER PAGE LAYOUT</div>

<section class="spread outer">
  <!-- back panel: telecoms climate -->
  <article class="panel white">
    <h2 class="heading abs climate-title">The Current<br>Telecoms Climate</h2>
    <div class="body-copy abs climate-copy">
      <p>The telecoms market, in relation to mobile phone masts, is going through some huge changes. Operators are combining to cut costs. We have already seen Northline join forces with Teleway and Aerion form a jointly owned company with Vantel called JMIL. More recently, Teleway and Brightcell have merged to form Unity Networks Ltd to become the new network leader. What this can mean for the landlord is changes to their site and potentially the loss of income. It can all be very confusing but don't worry, this is where we can help. We know the telecoms industry and understand how a new situation may affect a landlord, therefore, allowing us to provide the best advice on protecting your asset.</p>
      <p>In April 2017, the Government introduced the Digital Economy Act. This sets out significant changes for landlords, including the way rents are calculated. We have already seen operators contact landlords, trying to reduce their rent in light of this new law. We are working alongside specialist telecoms solicitors to try to reduce the potential negative impact on landlords.</p>
    </div>
    <svg class="fill-svg" width="211" height="489" viewBox="0 0 211 489" aria-hidden="true">
      <polygon points="0,363 211,363 211,489 0,489" fill="var(--green)" transform="translate(0,0)" opacity="0"/>
      <polygon points="0,364 211,378 211,489 0,489" fill="var(--lime)"/>
      <polygon points="0,376 211,380 211,489 0,489" fill="var(--green)"/>
    </svg>
    <p class="abs callout">Landlords should not sign anything until they have sought professional advice.</p>
  </article>

  <!-- middle panel: services & contact -->
  <article class="panel paper">
    <h2 class="heading abs services-title">Our Services</h2>
    <ul class="abs service-list">
      <li>Rent Reviews</li>
      <li>Lease Renewals</li>
      <li>Network Consolidation Issues</li>
      <li>Site Shares</li>
      <li>Rent Protection</li>
      <li>Equipment Upgrades</li>
      <li>Mast Removals / Decommissioning</li>
      <li>Mast Sales and Marketing</li>
      <li>Land Marketing for Masts</li>
      <li>Mast Management and Portfolios</li>
      <li>Safety Testing</li>
    </ul>
    <h2 class="heading abs contact-title">Contact Us</h2>
    <ul class="abs contact-list">
      <li><svg width="8" height="10" viewBox="0 0 8 10"><path d="M4 0a4 4 0 0 1 4 4c0 3-4 6-4 6S0 7 0 4a4 4 0 0 1 4-4z" fill="var(--green)"/><circle cx="4" cy="4" r="1.5" fill="var(--paper)"/></svg>Tallpoint Mast Advisers Ltd<br>The Old Granary,<br>Meadow Business Park,<br>Hill Cross,<br>Shropshire,<br>SY99 2ZZ</li>
      <li><svg width="8" height="8" viewBox="0 0 8 8"><path d="M1 0h2l1 2-1 1c.5 1 1 1.5 2 2l1-1 2 1v2c0 .5-.5 1-1 1C3 8 0 5 0 1c0-.5.5-1 1-1z" fill="var(--green)"/></svg>01632 960543</li>
      <li><svg width="9" height="8" viewBox="0 0 9 8"><rect x="2" y="0" width="5" height="2" fill="var(--green)"/><rect x="0" y="2" width="9" height="4" rx="1" fill="var(--green)"/><rect x="2" y="5" width="5" height="3" fill="var(--green)"/></svg>01632 960222</li>
      <li><svg width="9" height="7" viewBox="0 0 9 7"><rect width="9" height="7" fill="var(--green)"/><path d="M0 0l4.5 4L9 0" stroke="var(--paper)" fill="none" stroke-width=".8"/></svg>info@tallpointmast.co.uk</li>
      <li><svg width="8" height="8" viewBox="0 0 8 8"><circle cx="4" cy="4" r="3.6" fill="none" stroke="var(--green)" stroke-width=".9"/><ellipse cx="4" cy="4" rx="1.5" ry="3.6" fill="none" stroke="var(--green)" stroke-width=".8"/><path d="M.4 4h7.2" stroke="var(--green)" stroke-width=".8"/></svg>www.tallpointmast.co.uk</li>
    </ul>
    <div class="abs brand-mark brand-back"><span class="dot"></span><span>TALLPOINT<br>MAST ADVISERS</span></div>
  </article>

  <!-- front cover -->
  <article class="panel lime">
    <svg class="fill-svg" width="211" height="489" viewBox="0 0 211 489" role="img" aria-label="Photograph of a lattice phone mast standing on a green hillside under a bright blue sky">
      <defs>
        <linearGradient id="coverSky" x1="0" y1="0" x2="0" y2="1">
          <stop offset="0" stop-color="var(--sky-top)"/>
          <stop offset=".65" stop-color="var(--sky-low)"/>
          <stop offset=".78" stop-color="#5f8a3a"/>
          <stop offset="1" stop-color="#4b7a2c"/>
        </linearGradient>
      </defs>
      <polygon points="0,0 211,0 211,300 0,322" fill="url(#coverSky)"/>
      <polygon points="0,322 211,300 211,318 0,338" fill="var(--lime)"/>
    </svg>
    <div class="abs brand-mark brand-front"><span class="dot"></span><span>TALLPOINT<br>MAST ADVISERS</span></div>
    <h1 class="abs cover-headline"><span class="big">MARKET</span><span class="mid">YOUR POTENTIAL</span><span class="mid">PHONE MAST SITE!</span></h1>
    <div class="abs cover-rule"></div>
    <p class="abs cover-promise">We ACT EXCLUSIVELY for landlords<br>on ALL phone mast matters.</p>
    <div class="abs web-pill"><svg width="9" height="9" viewBox="0 0 8 8"><circle cx="4" cy="4" r="3.6" fill="none" stroke="#fff" stroke-width=".9"/><ellipse cx="4" cy="4" rx="1.5" ry="3.6" fill="none" stroke="#fff" stroke-width=".8"/><path d="M.4 4h7.2" stroke="#fff" stroke-width=".8"/></svg>www.tallpointmast.co.uk</div>
  </article>
</section>

<section class="spread inner">
  <!-- inner left -->
  <article class="panel white">
    <h2 class="heading abs firm-title">Tallpoint Mast Advisers is a firm of telecoms surveyors with over 15 years' experience of dealing with mobile phone mast operators.</h2>
    <div class="body-copy abs firm-copy">
      <p>We have built up a massive database of thousands of comparable mobile phone mast deals to aides in our telecoms negotiations. All our surveyors have spent time working for phone mast operators and know the industry inside out. <span class="accent">We now work exclusively for landlords</span>, fighting your corner, ensuring our landlords get the highest rents and best lease terms available in the market place.</p>
    </div>
    <svg class="fill-svg" width="211" height="489" viewBox="0 0 211 489" role="img" aria-label="Photograph looking up at a steel phone mast with antenna platforms against a blue sky">
      <defs>
        <linearGradient id="towerSky" x1="0" y1="0" x2="1" y2="1">
          <stop offset="0" stop-color="#1f62c8"/>
          <stop offset="1" stop-color="#9fc3ea"/>
        </linearGradient>
      </defs>
      <polygon points="0,252 211,252 211,489 0,489" fill="url(#towerSky)"/>
      <polygon points="0,252 211,252 211,238" fill="var(--lime)"/>
      <polygon points="0,252 0,262 211,252" fill="var(--green)"/>
    </svg>
  </article>

  <!-- inner middle -->
  <article class="panel lime">
    <div class="body-copy abs lease-copy">
      <p>Many of the original mobile phone mast leases / agreements are now coming up for renewal. This is an ideal opportunity for landlords to achieve the best deal. <strong>We are currently offering to review telecoms leases for free and provide landlords with our recommendations.</strong> If you would like to take us up on this free no obligation offer, send a copy of your agreement and any recent correspondence to us, either via post or email using the details on this flyer. Please also provide us with your name, contact number and let us know the current rent you are achieving so we can see if there is room for improvement. Once we have received this, one of our surveyors will give you a call when convenient to talk through your lease with you, highlighting anything we feel needs addressing, any opportunity to increase the rent, or to discuss a specific issue you are having with your mast (i.e. an upgrade request).</p>
    </div>
    <div class="body-copy abs lease-copy second">
      <p>Recently, operators have been attempting to cut costs by reducing rents. They are joining forces in an effort to drive rents down. Many landlords are contacting us after receiving a letter from the operators / operator's agent telling them they must accept a rent reduction or risk losing their site. In the majority of cases, Tallpoint Mast Advisers can prevent this from occurring and protect the landlord's rental income.</p>
    </div>
    <h2 class="heading abs sell-title">Sell your phone mast</h2>
    <div class="body-copy abs sell-copy">
      <p>We can also assist landlords in selling their phone mast. We have strong links with many large investors who regularly purchase the freehold or leasehold interest of masts and will pay a cash lump sum often, even hundreds of thousands of pounds.</p>
    </div>
  </article>

  <!-- inner right -->
  <article class="panel white">
    <svg class="fill-svg" width="211" height="489" viewBox="0 0 211 489" role="img" aria-label="Photograph of white panel antennas mounted on a mast pole against a blue sky with clouds">
      <defs>
        <linearGradient id="antennaSky" x1="0" y1="0" x2="0" y2="1">
          <stop offset="0" stop-color="#2a6bd0"/>
          <stop offset="1" stop-color="#a9cdf0"/>
        </linearGradient>
      </defs>
      <polygon points="0,0 211,0 211,207 0,228" fill="url(#antennaSky)"/>
      <polygon points="0,228 211,207 211,214 0,240" fill="var(--green)"/>
    </svg>
    <div class="body-copy abs cash-copy">
      <p>This can be done in a matter of weeks and the cash is yours to spend however you like, regardless of whether the mast stays for the duration of the investors leasehold or not. We can negotiate flexible terms, such as a buyback option so please call us today to discuss.</p>
    </div>
    <h2 class="heading abs getting-title">Getting a phone mast</h2>
    <div class="body-copy abs getting-copy">
      <p>If you don't currently have a mast located on your land but are interested in receiving thousands of pounds a year in rental income, or you have a redundant mast you would like to market, we offer a free advertising service on our website. We will market your land to phone mast operators with a view to having a mast located there. Please visit the 'Advertise My Site' link on our website to take advantage of this service.</p>
    </div>
  </article>
</section>

<div class="board-label inner">INNER PAGE LAYOUT</div>

</body>
</html>
```